Professional Oral Surgery Referral Pad, Business Card, and Stationary Design

Hello,

I want to work with a designer for my startup Oral Surgery Practice called: Dorrel Creek Oral Surgery & Implant Center

Ideally I would like to choose a good/professional design and work with a designer all the way to fulfill ALL of our stationary needs including referral pads, business cards, letterheads, envelopes, notepads, email signature, etc.

I would like to see designs first and hopefully would like to work with the designer for the lifetime of my practice and wanting to develop a long-term professional relationship.

In terms of the logo I have attached our practice logo files: I want to stay within the 3 colorways of the logo: Navy Blue/Silver grey/White. I would like for you to be creative and incorporate the "V" as best you can (for example greyed out watermark, etc)

I have also attached in my files the full contact info of our office in a word document: which includes address, email address, phone, fax, cell, etc.

I have also attached a few examples of double sided referral pad we can draw inspiration from. In terms of the referral pad I would ideally like to have my logo nicely placed/incorporated to make it look professional, address of the practice and contact info, my name and credentials.

Referral pad must have lines for patient, date of birth, phone number, referring doctor name, odontogram of all adult teeth and pediatric teeth, nice and big - so easy for dentist to refer. Also a jaw drawing of the intraoral cavity. Below that should have comments to surgeon.

In terms of procedures, I would like to have options of IV sedation, extractions, wisdom teeth, bone graft, pathology, tmj, trauma, expose/bond, orthognathic, other (list below)

In the back we can have a greyed out map of my practice address and Instructions for patients should include to bring insurance documentation, medication list, etc.

The final nitty gritty details of the referral pad can be worked on once I am happy with the design.

Target Market(s)

Patients who need oral surgical services and dentist referrals

Industry/Entity Type

Oral and Maxillofacial Surgery

• I would leave it up to the designers!

Colors
0054AA
0677BA
7BADD7
CADEEF
E8F1F8

Requirements
Must have
• Professional/sleek/modern and three color ways same as logo (navy blue, silver gray, and white)
Nice to have
• I would like to highlight my logo especially the implant ā€œvā€ either as watermark or part of the header or footnote. I will leave it to the expertise of the designer

```html
<!DOCTYPE html>
<html lang="en">
<head>
<meta charset="utf-8">
<title>Dorrel Creek Oral Surgery – Stationery Set</title>
<link rel="stylesheet" href="https://fonts.googleapis.com/css2?family=Cinzel:wght@600&family=Montserrat:wght@400;500;600;700&display=swap">
<style>
:root{
  --navy:#0f2590;
  --navy-deep:#0b1f7a;
  --royal:#1c45c9;
  --royal-dark:#1838b0;
  --sky:#9fd6ec;
  --silver:#b8bcc4;
  --ink:#0f1f6e;
  --paper:#ffffff;
  --paper-tint:#f3f6fb;
  --bg:#e6e7ea;
}
*{box-sizing:border-box;margin:0;padding:0}
html,body{width:1200px;height:494px;overflow:hidden;background:var(--bg);font-family:"Montserrat",sans-serif;color:var(--ink)}
.canvas{position:relative;width:1200px;height:494px}
.piece{position:absolute;overflow:hidden}
.wordmark{font-family:"Cinzel",serif;font-weight:600;white-space:nowrap;letter-spacing:.02em;line-height:1}
.wordmark.on-light{color:var(--navy)}
.wordmark.on-dark{color:var(--paper)}
.cross{position:absolute;color:var(--sky);font-weight:700;line-height:1}

/* Folder */
.folder-left{left:50px;top:45px;width:208px;height:281px;background:var(--royal-dark)}
.folder-right{left:258px;top:45px;width:209px;height:281px;background:var(--royal-dark)}
.folder-sheet{left:271px;top:53px;width:187px;height:180px;background:linear-gradient(160deg,var(--paper) 55%,var(--paper-tint))}
.folder-sheet .wordmark{position:absolute;left:12px;top:28px;font-size:14px}
.folder-sheet .tagline{position:absolute;left:12px;top:46px;font-size:4.3px;font-weight:600;color:var(--navy);letter-spacing:.02em;white-space:nowrap}
.pocket{background:var(--royal)}
.pocket-left{left:50px;top:233px;width:198px;height:93px;clip-path:polygon(0 0,95% 0,100% 100%,0 100%)}
.pocket-right{left:270px;top:233px;width:197px;height:93px;clip-path:polygon(5% 0,100% 0,100% 100%,0 100%)}
.pocket-right .wordmark{position:absolute;right:12px;top:37px;font-size:15px}

/* Letterhead */
.letterhead{left:494px;top:61px;width:187px;height:264px;background:linear-gradient(180deg,var(--paper),var(--paper-tint))}
.letterhead svg.header{position:absolute;left:0;top:0}
.letterhead .wordmark{position:absolute;left:12px;top:22px;font-size:13px}
.letterhead .tagline{position:absolute;left:12px;top:38px;font-size:4px;color:var(--paper);letter-spacing:.04em;white-space:nowrap}
.contact-list{position:absolute;list-style:none;font-size:3.6px;line-height:1.3;color:#5a6590}
.contact-list li{display:flex;gap:3px;margin-bottom:2.5px}
.contact-list svg{flex:none;margin-top:.5px}
.letterhead .contact-list{left:13px;top:218px}
.letterhead .date{position:absolute;right:17px;top:245px;font-size:4px;font-weight:600;color:var(--navy)}

/* Referral pad */
.referral{top:61px;width:223px;height:346px;background:var(--paper)}
.referral-front{left:692px}
.referral-back{left:925px}
.referral .wordmark{position:absolute;left:0;right:0;top:22px;text-align:center;font-size:21px}
.referral .headline{position:absolute;left:0;right:0;top:51px;text-align:center;font-family:"Cinzel",serif;font-weight:600;font-size:6.6px;line-height:1;white-space:nowrap;color:var(--navy)}
.referral .headline-rule{position:absolute;left:76px;width:72px;top:63px;height:.6px;background:var(--sky)}
.field{position:absolute;display:flex;align-items:flex-end;font-size:6px;color:var(--ink);white-space:nowrap}
.field .line{flex:1;border-bottom:.5px solid #7d86a8;margin-left:2px;height:5px}
.odontogram{position:absolute;left:30px;top:122px;width:176px;height:84px;border-radius:4px;background:linear-gradient(180deg,#f1f3f7,#e4e7ee)}
.section-title{position:absolute;font-size:6.6px;font-weight:600;color:var(--ink);white-space:nowrap}
.rule{position:absolute;left:19px;width:182px;height:.5px;background:#7d86a8}
.option{position:absolute;display:flex;align-items:center;gap:3px;font-size:6px;color:#5a6590;white-space:nowrap}
.option .box{width:4.5px;height:4.5px;border:.5px solid #5a6590}
.pad-footer{position:absolute;left:0;right:0;bottom:0;height:17px;background:var(--navy-deep);display:flex;justify-content:space-between;align-items:center;padding:0 19px 0 17px}
.pad-footer .contact-list{position:static;color:var(--paper);font-size:3.6px}
.pad-footer .contact-list li{margin:0}
.map{position:absolute;left:16px;top:135px;width:194px;height:136px;border-radius:4px;background:linear-gradient(135deg,#eceef2,#dcdfe5)}
.address-line{position:absolute;left:17px;top:276px;font-size:5.6px;color:var(--ink);white-space:nowrap}
.tick-line{position:absolute;left:17px;top:97px;display:flex;gap:3px;align-items:center;font-size:5.2px;color:#5a6590;white-space:nowrap}

/* Envelope */
.envelope{top:358px;width:196px;height:99px;background:var(--navy)}
.envelope-back{left:50px}
.envelope-back .wordmark{position:absolute;left:0;right:0;top:42px;text-align:center;font-size:16px}
.envelope-front{left:269px}
.envelope-front .flap{position:absolute;left:0;top:0;width:196px;height:27px}
.name-block{position:absolute;color:var(--paper);white-space:nowrap}
.name-block .name{font-weight:700;color:var(--silver);letter-spacing:.02em}
.envelope-front .name-block{left:14px;top:35px}
.envelope-front .name{font-size:5.8px}
.envelope-front .role{font-size:4px;margin-top:2px}
.envelope-front .contact-list{position:static;color:var(--paper);font-size:3.8px;margin-top:6px}

/* Business cards */
.card{top:354px;width:91px;height:53px;background:var(--navy)}
.card-front{left:495px}
.card-front .wordmark{position:absolute;left:0;right:0;top:21px;text-align:center;font-size:9.5px}
.card-back{left:591px}
.card-back .name-block{left:5px;top:13px}
.card-back .name{font-size:3.6px}
.card-back .role{font-size:2.4px;margin-top:1px}
.card-back .contact-list{position:static;color:var(--paper);font-size:2.3px;margin-top:3px}
.card-back .contact-list li{margin-bottom:1px}
</style>
</head>
<body>
<main class="canvas">

  <!-- Presentation folder -->
  <section class="piece folder-left"></section>
  <section class="piece folder-right"></section>
  <section class="piece folder-sheet">
    <span class="cross" style="right:40px;top:10px;font-size:7px">+</span>
    <span class="cross" style="right:30px;top:22px;font-size:5px">+</span>
    <span class="cross" style="left:8px;bottom:18px;font-size:7px">+</span>
    <div class="wordmark on-light">Dorrel Creek</div>
    <div class="tagline">DORREL CREEK ORAL SURGERY &amp; IMPLANT CENTER</div>
  </section>
  <section class="piece pocket pocket-left"></section>
  <section class="piece pocket pocket-right">
    <div class="wordmark on-dark">Dorrel Creek</div>
  </section>

  <!-- Letterhead -->
  <section class="piece letterhead">
    <svg class="header" width="187" height="90" viewBox="0 0 187 90" aria-hidden="true">
      <path d="M0 0H187V4L44 73Q22 82 0 76Z" fill="var(--navy)"/>
    </svg>
    <span class="cross" style="right:44px;top:6px;font-size:6px">+</span>
    <span class="cross" style="left:6px;top:156px;font-size:7px">+</span>
    <span class="cross" style="left:14px;top:168px;font-size:5px">+</span>
    <div class="wordmark on-dark">Dorrel Creek</div>
    <div class="tagline">DORREL CREEK ORAL SURGERY &amp; IMPLANT CENTER</div>
    <ul class="contact-list">
      <li><svg width="4" height="4" viewBox="0 0 10 10"><path d="M2 1l2 2-1 1.5q1 2 2.5 2.5L7 6l2 2-1.5 1.5Q3 9 .5 2.5Z" fill="#5a6590"/></svg><span>555 210 4471<br>555 210 4472</span></li>
      <li><svg width="4" height="4" viewBox="0 0 10 10"><circle cx="5" cy="5" r="4" fill="none" stroke="#5a6590" stroke-width="1.2"/><path d="M1 5h8M5 1v8" stroke="#5a6590"/></svg><span>info@dorrelcreekoms.com</span></li>
      <li><svg width="4" height="4" viewBox="0 0 10 10"><path d="M5 1L1 5h1.5v4h5V5H9Z" fill="#5a6590"/></svg><span>180 Alder Row<br>Dorrel Creek, CA 90000</span></li>
    </ul>
    <div class="date">07/08/2024</div>
  </section>

  <!-- Referral pad, front -->
  <section class="piece referral referral-front">
    <span class="cross" style="right:30px;top:6px;font-size:9px">+</span>
    <span class="cross" style="right:20px;top:20px;font-size:6px">+</span>
    <div class="wordmark on-light">Dorrel Creek</div>
    <div class="headline">DORREL CREEK ORAL SURGERY &amp; IMPLANT CENTER</div>
    <div class="headline-rule"></div>
    <div class="field" style="left:16px;top:83px;width:185px">Patient:<span class="line"></span></div>
    <div class="field" style="left:16px;top:97px;width:98px">Date of Birth:<span class="line"></span></div>
    <div class="field" style="left:115px;top:97px;width:86px">Patient Phone:<span class="line"></span></div>
    <div class="field" style="left:16px;top:112px;width:185px">Referred By Dr.:<span class="line"></span></div>
    <div class="odontogram" role="img" aria-label="Odontogram of adult and pediatric teeth with jaw drawing of the intraoral cavity"></div>
    <div class="section-title" style="left:19px;top:213px">Comments to Surgeon:</div>
    <div class="rule" style="top:228px"></div>
    <div class="rule" style="top:240px"></div>
    <div class="rule" style="top:251px"></div>
    <div class="rule" style="top:262px;width:115px"></div>
    <div class="section-title" style="left:19px;top:273px">Procedures:</div>
    <div class="option" style="left:19px;top:285px"><span class="box"></span>IV Sedation</div>
    <div class="option" style="left:89px;top:285px"><span class="box"></span>TMJ</div>
    <div class="option" style="left:159px;top:285px"><span class="box"></span>Trauma</div>
    <div class="option" style="left:19px;top:297px"><span class="box"></span>Extractions</div>
    <div class="option" style="left:89px;top:297px"><span class="box"></span>Pathology</div>
    <div class="option" style="left:159px;top:297px"><span class="box"></span>Expose/Bond</div>
    <div class="option" style="left:19px;top:308px"><span class="box"></span>Bone Graft</div>
    <div class="option" style="left:89px;top:308px"><span class="box"></span>Wisdom Teeth</div>
    <div class="option" style="left:159px;top:308px"><span class="box"></span>Orthognathic</div>
    <footer class="pad-footer">
      <ul class="contact-list"><li>555 210 4471<br>555 210 4472</li></ul>
      <ul class="contact-list"><li>180 Alder Row<br>Dorrel Creek, CA 90000</li></ul>
    </footer>
  </section>

  <!-- Referral pad, back -->
  <section class="piece referral referral-back">
    <span class="cross" style="right:30px;top:6px;font-size:9px">+</span>
    <span class="cross" style="right:20px;top:20px;font-size:6px">+</span>
    <div class="wordmark on-light">Dorrel Creek</div>
    <div class="headline">DORREL CREEK ORAL SURGERY &amp; IMPLANT CENTER</div>
    <div class="headline-rule"></div>
    <div class="section-title" style="left:17px;top:86px">INSTRUCTIONS TO PATIENTS:</div>
    <div class="tick-line"><svg width="6" height="5" viewBox="0 0 12 10"><path d="M1 5l3.5 3.5L11 1" fill="none" stroke="#5a6590" stroke-width="1.6"/></svg>Please bring MEDICAL and DENTAL Insurance information with you</div>
    <div class="section-title" style="left:17px;top:121px">LOCATION VIEW</div>
    <div class="map" role="img" aria-label="Greyed-out street map showing the practice location"></div>
    <div class="address-line">180 Alder Row, Dorrel Creek, CA 90000</div>
    <footer class="pad-footer">
      <ul class="contact-list"><li>555 210 4471<br>555 210 4472</li></ul>
      <ul class="contact-list"><li>180 Alder Row<br>Dorrel Creek, CA 90000</li></ul>
    </footer>
  </section>

  <!-- Envelope back -->
  <section class="piece envelope envelope-back">
    <span class="cross" style="right:16px;top:2px;font-size:9px">+</span>
    <span class="cross" style="right:46px;top:12px;font-size:9px">+</span>
    <span class="cross" style="left:2px;bottom:26px;font-size:8px">+</span>
    <span class="cross" style="left:8px;bottom:6px;font-size:10px">+</span>
    <div class="wordmark on-dark">Dorrel Creek</div>
  </section>

  <!-- Envelope front -->
  <section class="piece envelope envelope-front">
    <svg class="flap" viewBox="0 0 196 27" aria-hidden="true">
      <path d="M0 0H196V12Q196 27 180 27H14Q0 27 0 13Z" fill="var(--royal-dark)"/>
    </svg>
    <div class="name-block">
      <div class="name">DR. ANYA CORWELL, DDS</div>
      <div class="role">Dorrel Creek Oral Surgery &amp; Implant Center</div>
      <ul class="contact-list">
        <li>555 210 4471<br>555 210 4472</li>
        <li>info@dorrelcreekoms.com</li>
        <li>180 Alder Row<br>Dorrel Creek, CA 90000</li>
      </ul>
    </div>
  </section>

  <!-- Business card front -->
  <section class="piece card card-front">
    <span class="cross" style="right:16px;top:2px;font-size:7px">+</span>
    <span class="cross" style="left:4px;bottom:3px;font-size:6px">+</span>
    <div class="wordmark on-dark">Dorrel Creek</div>
  </section>

  <!-- Business card back -->
  <section class="piece card card-back">
    <span class="cross" style="right:14px;top:2px;font-size:7px">+</span>
    <div class="name-block">
      <div class="name">DR. ANYA CORWELL, DDS</div>
      <div class="role">Dorrel Creek Oral Surgery &amp; Implant Center</div>
      <ul class="contact-list">
        <li>555 210 4471<br>555 210 4472</li>
        <li>info@dorrelcreekoms.com</li>
        <li>180 Alder Row<br>Dorrel Creek, CA 90000</li>
      </ul>
    </div>
  </section>

</main>
</body>
</html>
```